RW Frameworks Inc Business cards

We need business cards using our existing logo but slightly modified. Right now the logo says RW Framework Masonry. We want to keep the RW part of the design, but replace the Framework Masonry portion with "FRAMEWORKS". Please see the attached file.
Ideally this would be a blank template so we can add Different Names, titles, and phone numbers later.
On the one side we want only the logo and on the other side the detail. I'm attaching an example for you to see.
Please reach out with any other questions. Our address and other details will be given out once we find a design we like.

Target Market(s)

Construction Industry

```html
<!DOCTYPE html>
<html lang="en">
<head>
<meta charset="utf-8">
<title>RW Frameworks Inc — Business Cards</title>
<link rel="stylesheet" href="https://fonts.googleapis.com/css2?family=Roboto:wght@400;500;700&display=swap">
<style>
  :root {
    --backdrop: #5b80b9;
    --brand-blue: #2b5fa8;
    --brand-blue-deep: #1f4f96;
    --brand-blue-dark: #1d4a8c;
    --card-white: #f7f7f5;
    --ink-grey: #5e5e5e;
    --ink-mid: #6f6f6f;
  }
  * { box-sizing: border-box; margin: 0; padding: 0; }
  html, body {
    width: 1200px;
    height: 852px;
    overflow: hidden;
  }
  body {
    background: var(--backdrop);
    font-family: "Roboto", Arial, sans-serif;
    position: relative;
  }
  .card {
    position: absolute;
    top: 268px;
    width: 540px;
    height: 316px;
    border-radius: 22px;
  }
  .card--front {
    left: 40px;
    background: var(--brand-blue);
    display: flex;
    align-items: center;
    justify-content: center;
  }
  .card--back {
    left: 620px;
    background: var(--card-white);
  }
  .wordmark {
    font-family: "Roboto", Arial, sans-serif;
    font-weight: 700;
    letter-spacing: 4px;
    line-height: 1;
    text-transform: uppercase;
    display: flex;
    align-items: center;
    gap: 12px;
  }
  .wordmark__square {
    width: 14px;
    height: 14px;
  }
  .card--front .wordmark {
    font-size: 44px;
    color: var(--brand-blue-dark);
  }
  .card--front .wordmark__square { background: var(--brand-blue-dark); width: 20px; height: 20px; }
  .card--back .wordmark {
    position: absolute;
    left: 34px;
    top: 180px;
    font-size: 24px;
    letter-spacing: 2.5px;
    color: var(--brand-blue);
  }
  .card--back .wordmark__square { background: var(--ink-grey); }
  .details {
    position: absolute;
    left: 300px;
    top: 56px;
    width: 220px;
    color: var(--ink-grey);
  }
  .details__name {
    font-size: 19px;
    font-weight: 700;
    color: var(--brand-blue);
  }
  .details__title {
    font-size: 12.5px;
    color: var(--ink-mid);
    margin: 3px 0 0 16px;
  }
  .details__list {
    list-style: none;
    margin-top: 22px;
    font-size: 12px;
    line-height: 1.55;
  }
  .details__item {
    display: flex;
    align-items: center;
    gap: 10px;
  }
  .details__icon {
    width: 11px;
    height: 11px;
    fill: var(--brand-blue-deep);
    flex: none;
  }
  .details__address {
    margin: 6px 0 0 21px;
    font-size: 12px;
    line-height: 1.55;
  }
</style>
</head>
<body>
  <section class="card card--front" aria-label="Card front">
    <div class="wordmark"><span class="wordmark__square"></span>RW Frameworks</div>
  </section>

  <section class="card card--back" aria-label="Card back">
    <div class="wordmark"><span class="wordmark__square"></span>RW Frameworks</div>

    <div class="details">
      <h1 class="details__name">John RW Smith</h1>
      <p class="details__title">Managing Director</p>
      <ul class="details__list">
        <li class="details__item">
          <svg class="details__icon" viewBox="0 0 12 12" aria-hidden="true"><path d="M2 1h2l1 3-1.5 1a7 7 0 0 0 3.5 3.5L8 7l3 1v2a1 1 0 0 1-1 1A9 9 0 0 1 1 2a1 1 0 0 1 1-1z"/></svg>
          555-014-2290
        </li>
        <li class="details__item">
          <svg class="details__icon" viewBox="0 0 12 12" aria-hidden="true"><path d="M1 2.5h10v7H1z M1.4 3l4.6 3.6L10.6 3" stroke="#f7f7f5" stroke-width="0.9"/></svg>
          john@rwframeworks-example.com
        </li>
        <li class="details__item">
          <svg class="details__icon" viewBox="0 0 12 12" aria-hidden="true"><circle cx="6" cy="6" r="5"/><path d="M1 6h10M6 1c-2 2.5-2 7.5 0 10M6 1c2 2.5 2 7.5 0 10" stroke="#f7f7f5" stroke-width="0.7" fill="none"/></svg>
          www.rwframeworks-example.com
        </li>
      </ul>
      <p class="details__address">418 Ridgeline Ave., Brookvale,<br>California, US 900210</p>
    </div>
  </section>
</body>
</html>
```